Velloran Winery Wine Label Re-design

Velloran Winery is located in the Finger Lakes region of New York. The Calloway Family planted the first vineyards in 1979 and opened in 1986. We produce award winning premium, hand crafted estate grown wines. We are in the process of a wine label re-design across our entire line. We would like to have the new label 'pop' but still convey elegance and ultra-premium quality. We are open to all color and styles or a minimalist design.
The attached files contain our new logo and samples of our current label (marked current) with dimensions. Our labeler is limited to label shapes but does not necessarily to have to be die-cut(the top arch) like our current label.

Target Market(s)

Upper income quality wine drinkers

Colors

Designer to choose colors to be used in the design.

Requirements
Should not have
• Should not be a tranparent label

```html
<!DOCTYPE html>
<html lang="en">
<head>
<meta charset="utf-8">
<title>Velloran Winery – Wine Labels</title>
<link rel="stylesheet" href="https://fonts.googleapis.com/css2?family=Cinzel:wght@400;500&display=swap">
<style>
  :root {
    --backdrop-top: #b4b4b4;
    --backdrop-bottom: #a6a6a6;
    --label-paper: #fbfbfa;
    --brand-maroon: #7a2a3c;
    --brand-muted: #8a6470;
    --red-band: #0b0b0b;
    --white-band: #7fae8c;
    --red-type: #f2f0ec;
    --white-type: #1e2a22;
  }
  * { margin: 0; padding: 0; box-sizing: border-box; }
  html, body { width: 801px; height: 1200px; overflow: hidden; }
  body {
    background: linear-gradient(var(--backdrop-top), var(--backdrop-bottom));
    font-family: "Cinzel", "Times New Roman", serif;
  }
  .label-set {
    position: absolute;
    left: 40px; top: 335px;
    display: flex; gap: 41px;
  }
  .wine-label {
    position: relative;
    width: 340px; height: 530px;
    background: var(--label-paper);
    overflow: hidden;
    box-shadow: 0 2px 6px rgba(0,0,0,0.15);
  }
  .band { position: absolute; left: 0; top: 0; width: 340px; height: 530px; }
  .brand {
    position: absolute; top: 52px; left: 0; right: 0;
    text-align: center; color: var(--brand-maroon);
  }
  .brand-mark {
    display: block; margin: 0 auto 16px;
    width: 50px; height: 50px;
    border: 2px solid var(--brand-maroon); border-radius: 50%;
  }
  .brand-name {
    font-size: 30px; font-weight: 400; letter-spacing: 7px; line-height: 1;
  }
  .brand-sub {
    font-size: 13px; letter-spacing: 8px; color: var(--brand-muted); margin-top: 5px;
  }
  .varietal {
    position: absolute; right: 8px;
    font-size: 22px; line-height: 1.1; letter-spacing: 0.5px; white-space: nowrap;
  }
  .vintage {
    position: absolute;
    font-size: 14px; letter-spacing: 9px;
  }
  .label-red .varietal { left: 170px; top: 432px; color: var(--red-type); }
  .label-red .vintage { left: 172px; top: 494px; color: var(--red-type); }
  .label-white .varietal { left: 152px; top: 470px; color: var(--white-type); }
  .label-white .vintage { left: 154px; top: 500px; color: var(--white-type); }
</style>
</head>
<body>
  <main class="label-set">
    <section class="wine-label label-red">
      <svg class="band" viewBox="0 0 340 530" aria-hidden="true">
        <path d="M0 516 C110 490 170 340 340 312 L340 530 L0 530 Z" fill="var(--red-band)"/>
      </svg>
      <header class="brand">
        <span class="brand-mark"></span>
        <div class="brand-name">VELLORAN</div>
        <div class="brand-sub">WINERY</div>
      </header>
      <p class="varietal">CABERNET<br>SAUVIGNON</p>
      <p class="vintage">2013</p>
    </section>

    <section class="wine-label label-white">
      <svg class="band" viewBox="0 0 340 530" aria-hidden="true">
        <path d="M0 520 C90 490 150 345 250 328 C295 320 322 338 340 362 L340 530 L0 530 Z" fill="var(--white-band)"/>
      </svg>
      <header class="brand">
        <span class="brand-mark"></span>
        <div class="brand-name">VELLORAN</div>
        <div class="brand-sub">WINERY</div>
      </header>
      <p class="varietal">CHARDONNAY</p>
      <p class="vintage">2013</p>
    </section>
  </main>
</body>
</html>
```